Stylish, Masculine Design - Men's Clothing

Granary Coat Mart is a 14,000 square foot warehouse outlet store open to the public since 2005. 50+ brands. Well-known designer brand names and private labels. 30-80% off retail everyday. Lowest prices guaranteed. Average suit price $150. Average shirt price $20. One-stop shop shopping. Men's suits, tuxedos, tuxedo rentals, dress shirts, ties, dress shoes, boy's suits and tuxedos, clergy robes, clergy shirts, cologne, loungewear. Slim fits (Prom Dance), business styles, "church" fashion, security-related uniform. Alterations done by expert tailors on premises for an extra charge.
The final design for both business card and logo should portray stylishness and masculinity.
Updates
We will be changing our name. Details below.New name: Warehouse Suit & TuxFormer name: Granary Coat Mart Added Monday, December 26, 2016
Target Market(s)
Gender: 80% Male, 15% Female, 5% Transgender
Location: 80% 10 Mile Radius, 20% >10 Mile Radius
Age: 17-18 (Primarily prom), 18-35 (Primarily Interviews and Weddings), 36-70 (primarily Church and events)
Race: African-American 50%, Latino-American 20%, White 15%, 10% Asian 5% Other
Religions: Christian 50%, 20% Catholic, 10% Mormon, 20% Other/None
Occupation: Local government 40%, Large corporation employee 20%, Small business employee 10%, Small business owner 10%, 20% Unemployed (high school, college)
Education: High School or equivalent 40%, College 30%, Some College 20%, Masters/Doctors 10%
Industry/Entity Type
Retail
Contact Information for Business Card
Name: Peter Olund
Title: Sales Associate
Address: 418 E. Mirabeth Ave. Harlow Springs, CA 91877
Phone Number: 310.555.0182
Slogan: Broad Racks. Fair Prices, Friendly Fitting Help
www.granarycoatmart.example
Logo Text
GCM (Acronym for Granary Coat Mart) or Image
Requirements
Must have
- Easy to read
- Visually appealing

```html
<!DOCTYPE html>
<html lang="en">
<head>
<meta charset="utf-8">
<title>Granary Coat Mart – Business Card</title>
<link rel="stylesheet" href="https://fonts.googleapis.com/css2?family=Open+Sans:wght@400;600;700&display=swap">
<style>
  :root {
    --brand-red: #ec1f27;
    --ink: #111111;
    --grey-text: #333333;
    --paper: #ffffff;
    --backdrop: #e9e6e1;
  }
  * { box-sizing: border-box; margin: 0; padding: 0; }
  html, body {
    width: 1200px; height: 900px; overflow: hidden;
    background: var(--backdrop);
    font-family: "Open Sans", Arial, sans-serif;
  }
  .sheet {
    position: relative; width: 1200px; height: 900px;
    display: flex; flex-direction: column; align-items: center; justify-content: center; gap: 40px;
  }
  .card {
    position: relative; width: 640px; height: 366px; overflow: hidden;
    box-shadow: 0 6px 18px rgba(0,0,0,0.18);
  }

  /* Front */
  .card--front { background: var(--brand-red); color: var(--paper); }
  .card--front .wordmark {
    position: absolute; left: 0; right: 0; top: 70px;
    text-align: center; font-weight: 700; font-size: 56px; line-height: 1.02;
    letter-spacing: 1px; text-transform: uppercase; color: var(--paper);
  }
  .card--front .slogan {
    position: absolute; left: 0; right: 0; top: 232px;
    text-align: center; font-weight: 600; font-size: 15px; letter-spacing: 0.6px;
    text-transform: uppercase; color: var(--paper);
  }

  /* Back */
  .card--back { background: var(--paper); color: var(--grey-text); }
  .card--back .decor { position: absolute; inset: 0; }
  .holder { position: absolute; left: 76px; top: 22px; }
  .holder__name { color: var(--brand-red); font-weight: 700; font-size: 19px; line-height: 1.1; }
  .holder__title { font-size: 13px; color: var(--grey-text); }
  .contact { position: absolute; left: 40px; top: 146px; font-size: 14.5px; line-height: 1.45; color: var(--grey-text); }
  .contact__row { display: flex; align-items: center; gap: 8px; }
  .contact__row svg { width: 12px; height: 12px; flex: none; }
  .contact__address { margin-bottom: 4px; }
  .card--back .wordmark {
    position: absolute; right: 36px; top: 132px; width: 290px;
    text-align: center; font-weight: 700; font-size: 40px; line-height: 1.05;
    letter-spacing: 1px; text-transform: uppercase; color: var(--ink);
  }
</style>
</head>
<body>
<main class="sheet">

  <section class="card card--front" aria-label="Card front">
    <p class="wordmark">Granary<br>Coat Mart</p>
    <p class="slogan">Broad Racks. Fair Prices, Friendly Fitting Help</p>
  </section>

  <section class="card card--back" aria-label="Card back">
    <svg class="decor" viewBox="0 0 640 366" aria-hidden="true">
      <polygon points="0,0 64,0 56,22 0,22" fill="var(--brand-red)"/>
      <polygon points="28,44 58,0 64,0 64,44" fill="var(--ink)"/>
      <polygon points="0,262 300,262 288,290 0,290" fill="var(--brand-red)"/>
      <polygon points="302,300 640,300 640,366 276,366" fill="var(--ink)"/>
    </svg>

    <div class="holder">
      <p class="holder__name">Peter Olund</p>
      <p class="holder__title">Sales Associate</p>
    </div>

    <div class="contact">
      <p class="contact__address">418 E. Mirabeth Ave. Harlow Springs,<br>CA 91877</p>
      <p class="contact__row">
        <svg viewBox="0 0 12 12" aria-hidden="true"><path d="M2.5 1 L4.5 1 L5 3.5 L3.8 4.5 Q5 7 7.5 8.2 L8.5 7 L11 7.5 L11 9.5 Q10.5 11 9 11 Q1 10 1 2.5 Q1 1 2.5 1 Z" fill="var(--brand-red)"/></svg>
        310.555.0182
      </p>
      <p class="contact__row">
        <svg viewBox="0 0 12 12" aria-hidden="true"><circle cx="6" cy="6" r="5" fill="none" stroke="var(--brand-red)" stroke-width="1.4"/><path d="M1 6 H11 M6 1 Q3 6 6 11 M6 1 Q9 6 6 11" fill="none" stroke="var(--brand-red)" stroke-width="1"/></svg>
        www.granarycoatmart.example
      </p>
    </div>

    <p class="wordmark">Granary<br>Coat Mart</p>
  </section>

</main>
</body>
</html>
```